Brightfield Co Trade Show Flyer

We need a brochure design (8.5 x 11) Info in the design (refer to rough draft I drew on Paper): "#1 selling tool to aquire new franchisees has been video testimonials" - Martin L. Crowe, C.E.O Tovik Smoothie Franchise Testimonials - Let your franchisees do the selling for you. Franchisee testimonial: $10,000 / per Franchisee Includes: • 2 minute Video • 1 minute add for your franchise's location • Concept creation • Communication with franchisee • Travel to their location • All rental equipment • 1 round of corrections • Animated logo • Licensed music ******* For 25% Discount section (next to middle box), please put the "Outlet Summit Logo" Great to use on all your social media (USE logos and icons) • Website • Vidloop • Workwave • Friendly • Snapsy • Chirper • Phone calls • Emails • In person meetings Some of our clients: (use the logos I uploaded - in round boxes as in draft) LOGO (Brightfield Franchise Testimonial) www.brightfieldvoices.example (866) 555-0172

Target Market(s)

Franchise owners

Colors

Designer to choose colors to be used in the design.

Requirements

```html
<!DOCTYPE html>
<html lang="en">
<head>
<meta charset="utf-8">
<title>Brightfield Co – Franchise Testimonials Flyer</title>
<link rel="stylesheet" href="https://fonts.googleapis.com/css2?family=Oswald:wght@700&family=Open+Sans:wght@400;600;700;800&display=swap">
<style>
:root{
  --page-bg:#d6d6d6;
  --paper:#ffffff;
  --red:#d0181e;
  --red-dark:#8e0d10;
  --ink:#1c1c1c;
  --ink-soft:#444;
  --green:#16a88a;
  --band:#ecebec;
  --card:#e7e6e8;
}
*{box-sizing:border-box;margin:0;padding:0}
html,body{width:703px;height:1200px;overflow:hidden;background:var(--page-bg);font-family:"Open Sans",Arial,sans-serif;color:var(--ink)}
.flyer{position:absolute;left:21px;top:173px;width:660px;height:854px;background:var(--paper);box-shadow:8px 8px 10px rgba(0,0,0,.35);overflow:hidden}

/* hero */
.hero{position:absolute;left:0;top:0;width:660px;height:294px;background:radial-gradient(ellipse at 30% 40%,#2e4a6e 0%,#0f1a2a 35%,#050608 70%),#000}
.hero-photo{position:absolute;left:40px;top:18px;width:250px;height:276px;background:radial-gradient(ellipse at 60% 40%,rgba(170,190,215,.55),rgba(40,60,90,.25) 55%,transparent 75%)}
.hero-title{position:absolute;left:313px;top:82px;font-family:"Oswald",Impact,sans-serif;font-weight:700;line-height:1;letter-spacing:-.5px}
.hero-title .l1{display:block;color:var(--red);font-size:64px;transform:scaleX(.92);transform-origin:left}
.hero-title .l2{display:block;color:#fff;font-size:52px;margin-top:2px;transform:scaleX(.92);transform-origin:left}
.hero-sub{position:absolute;left:315px;top:206px;color:#fff;font-size:14.5px;font-weight:600}
.hero-stripe{position:absolute;left:0;top:296px;width:660px;height:7px;background:var(--red)}

/* event name */
.summit{position:absolute;left:27px;top:368px;width:292px;display:flex;align-items:center;justify-content:center;gap:9px;color:var(--green);font-size:24px;font-weight:800;line-height:1}
.summit::before{content:"";width:22px;height:22px;background:var(--green);flex:none}

/* discount */
.discount{position:absolute;left:27px;top:451px;width:292px;height:125px}
.discount-text{position:absolute;left:20px;top:46px;width:130px;text-align:center;color:#fff;line-height:1}
.discount-text b{display:block;font-size:23px;font-weight:700}
.discount-text span{display:block;font-size:15px;margin-top:3px}
.discount-pct{position:absolute;left:153px;top:40px;width:112px;text-align:center;color:#fff;font-size:42px;font-weight:700;letter-spacing:-1px}

/* social */
.social{position:absolute;left:27px;top:604px;display:flex;gap:9px;list-style:none}
.social li{display:flex;align-items:center;gap:3px;font-size:9.5px;font-weight:700;color:var(--ink-soft)}
.social li::before{content:"";width:9px;height:9px;background:var(--red)}

/* quote */
.quote{position:absolute;left:366px;top:334px;width:270px}
.quote p{position:relative;padding-left:29px;font-size:15px;line-height:1.22;color:var(--ink)}
.quote .q{position:absolute;font-family:Georgia,serif;font-weight:700;font-size:30px;line-height:1;color:var(--ink)}
.quote .q.open{left:0;top:-6px}
.quote .q.close{left:128px;top:38px}
.quote cite{display:block;text-align:right;font-style:normal;margin-top:-6px}
.quote cite b{color:var(--red);font-size:12px}
.quote cite small{display:block;font-size:8px;color:var(--ink)}

/* price card */
.price{position:absolute;left:368px;top:423px;width:266px;height:213px;background:var(--card);border-radius:6px;overflow:hidden}
.price-head{position:absolute;left:0;top:0;width:266px;height:80px}
.price-amount{position:absolute;left:0;top:8px;width:266px;text-align:center;color:#fff;line-height:1}
.price-amount b{display:block;font-size:28px;font-weight:700}
.price-amount b sup{font-size:17px;vertical-align:9px}
.price-amount span{display:block;font-size:14px;font-weight:600;margin-top:2px}
.includes{position:absolute;top:92px;list-style:none;font-size:9.5px;line-height:1.12;color:var(--ink-soft)}
.includes.col-a{left:20px;width:118px}
.includes.col-b{left:142px;width:118px}
.includes li{position:relative;padding-left:15px;margin-bottom:6px}
.includes svg{position:absolute;left:0;top:1px}

/* trusted */
.trusted{position:absolute;left:0;top:660px;width:660px;height:74px;background:var(--band);display:flex;align-items:center;padding-left:29px}
.trusted h3{font-size:13.5px;font-weight:700;color:var(--ink-soft);width:125px;letter-spacing:.3px}
.clients{display:flex;list-style:none;align-items:center}
.clients li{font-size:11px;font-weight:700;color:var(--ink-soft);padding:0 11px;border-left:2px solid #fff;height:48px;display:flex;align-items:center;text-align:center;line-height:1.15}
.clients li:first-child{border-left:0;padding-left:0}
.trusted-shadow{position:absolute;left:110px;top:734px;width:440px;height:10px;background:radial-gradient(ellipse at 50% 0,rgba(0,0,0,.28),transparent 70%)}

/* footer */
.footer{position:absolute;left:0;top:758px;width:660px;height:96px}
.brand{position:absolute;left:26px;top:800px;width:170px;text-align:center;color:#fff;font-weight:800}
.brand .mark{display:block;width:22px;height:22px;border-radius:50%;background:#fff;margin:0 auto 5px}
.brand .name{font-size:17px;letter-spacing:.3px}
.contact{position:absolute;left:288px;top:802px;color:#fff}
.contact .phone{display:flex;align-items:center;gap:6px;font-size:19px;font-weight:600;letter-spacing:.3px}
.contact .lines{display:flex;gap:12px;margin-top:5px;font-size:8.5px}
.contact .lines span{display:flex;align-items:center;gap:5px}
.icon-ring{width:17px;height:17px;border:1.3px solid #fff;border-radius:50%;display:inline-flex;align-items:center;justify-content:center;flex:none}
.lines .icon-ring{width:15px;height:15px}
</style>
</head>
<body>
<main class="flyer">

  <header class="hero">
    <div class="hero-photo" role="img" aria-label="Vintage film projector with reels lit by a bright beam"></div>
    <h1 class="hero-title"><span class="l1">FRANCHISE</span><span class="l2">TESTIMONIALS</span></h1>
    <p class="hero-sub">Let your franchisees do the selling for you</p>
  </header>
  <div class="hero-stripe"></div>

  <div class="summit">Outlet Summit</div>

  <div class="discount">
    <svg width="292" height="125" viewBox="0 0 292 125">
      <defs>
        <linearGradient id="hexRed" x1="0" y1="0" x2="0" y2="1">
          <stop offset="0" stop-color="#e0262c"/><stop offset="1" stop-color="#8e0d10"/>
        </linearGradient>
        <linearGradient id="bandBlack" x1="0" y1="0" x2="0" y2="1">
          <stop offset="0" stop-color="#1a1a1a"/><stop offset="1" stop-color="#000"/>
        </linearGradient>
      </defs>
      <polygon points="0,25 290,25 280,62 290,100 14,100 6,62" fill="url(#bandBlack)"/>
      <polygon points="210,0 266,31 266,94 210,125 154,94 154,31" fill="url(#hexRed)" stroke="#fff" stroke-width="2"/>
    </svg>
    <div class="discount-text"><b>DISCOUNT</b><span>FOR</span></div>
    <div class="discount-pct">25%</div>
  </div>

  <ul class="social">
    <li>Vidloop</li><li>Workwave</li><li>Friendly</li><li>Snapsy</li><li>Chirper</li>
  </ul>

  <blockquote class="quote">
    <p><span class="q open">“</span>#1 selling tool to aquire new franchisees has been video testimonials<span class="q close">”</span></p>
    <cite><b>....Martin L. Crowe</b><small>C.E.O Tovik Smoothie</small></cite>
  </blockquote>

  <section class="price">
    <svg class="price-head" width="266" height="80" viewBox="0 0 266 80">
      <defs>
        <linearGradient id="headRed" x1="0" y1="0" x2="0" y2="1">
          <stop offset="0" stop-color="#e0262c"/><stop offset="1" stop-color="#a51115"/>
        </linearGradient>
      </defs>
      <path d="M0 0H266V44H210Q190 44 180 60Q165 76 133 76Q101 76 86 60Q76 44 56 44H0Z" fill="url(#headRed)"/>
    </svg>
    <div class="price-amount"><b><sup>$</sup>10,000</b><span>Per Franchisee</span></div>
    <ul class="includes col-a">
      <li><svg width="11" height="11" viewBox="0 0 11 11"><circle cx="5.5" cy="5.5" r="4.6" fill="none" stroke="#555" stroke-width="1.1"/><path d="M3 5.6l1.8 1.8L9.5 2.5" fill="none" stroke="#555" stroke-width="1.3"/></svg>2 minute Video</li>
      <li><svg width="11" height="11" viewBox="0 0 11 11"><circle cx="5.5" cy="5.5" r="4.6" fill="none" stroke="#555" stroke-width="1.1"/><path d="M3 5.6l1.8 1.8L9.5 2.5" fill="none" stroke="#555" stroke-width="1.3"/></svg>1 minute add for your franchise's location</li>
      <li><svg width="11" height="11" viewBox="0 0 11 11"><circle cx="5.5" cy="5.5" r="4.6" fill="none" stroke="#555" stroke-width="1.1"/><path d="M3 5.6l1.8 1.8L9.5 2.5" fill="none" stroke="#555" stroke-width="1.3"/></svg>Concept creation</li>
      <li><svg width="11" height="11" viewBox="0 0 11 11"><circle cx="5.5" cy="5.5" r="4.6" fill="none" stroke="#555" stroke-width="1.1"/><path d="M3 5.6l1.8 1.8L9.5 2.5" fill="none" stroke="#555" stroke-width="1.3"/></svg>Communication with franchisee</li>
    </ul>
    <ul class="includes col-b">
      <li><svg width="11" height="11" viewBox="0 0 11 11"><circle cx="5.5" cy="5.5" r="4.6" fill="none" stroke="#555" stroke-width="1.1"/><path d="M3 5.6l1.8 1.8L9.5 2.5" fill="none" stroke="#555" stroke-width="1.3"/></svg>Travel to their location</li>
      <li><svg width="11" height="11" viewBox="0 0 11 11"><circle cx="5.5" cy="5.5" r="4.6" fill="none" stroke="#555" stroke-width="1.1"/><path d="M3 5.6l1.8 1.8L9.5 2.5" fill="none" stroke="#555" stroke-width="1.3"/></svg>All rental equipment</li>
      <li><svg width="11" height="11" viewBox="0 0 11 11"><circle cx="5.5" cy="5.5" r="4.6" fill="none" stroke="#555" stroke-width="1.1"/><path d="M3 5.6l1.8 1.8L9.5 2.5" fill="none" stroke="#555" stroke-width="1.3"/></svg>1 round of corrections</li>
      <li><svg width="11" height="11" viewBox="0 0 11 11"><circle cx="5.5" cy="5.5" r="4.6" fill="none" stroke="#555" stroke-width="1.1"/><path d="M3 5.6l1.8 1.8L9.5 2.5" fill="none" stroke="#555" stroke-width="1.3"/></svg>Animated logo</li>
      <li><svg width="11" height="11" viewBox="0 0 11 11"><circle cx="5.5" cy="5.5" r="4.6" fill="none" stroke="#555" stroke-width="1.1"/><path d="M3 5.6l1.8 1.8L9.5 2.5" fill="none" stroke="#555" stroke-width="1.3"/></svg>Licensed music ***</li>
    </ul>
  </section>

  <section class="trusted">
    <h3>TRUSTED BY:</h3>
    <ul class="clients">
      <li>Corrin<br>Creamery</li>
      <li>Dayline<br>Mart</li>
      <li>Tovik<br>Smoothie</li>
      <li>Neatwell<br>Cleaning</li>
      <li>Gearline<br>Auto</li>
    </ul>
  </section>
  <div class="trusted-shadow"></div>

  <svg class="footer" width="660" height="96" viewBox="0 0 660 96">
    <defs>
      <linearGradient id="footRed" x1="0" y1="0" x2="0" y2="1">
        <stop offset="0" stop-color="#e0262c"/><stop offset="1" stop-color="#8e0d10"/>
      </linearGradient>
      <linearGradient id="footDark" x1="0" y1="0" x2="0" y2="1">
        <stop offset="0" stop-color="#555"/><stop offset="1" stop-color="#0d0d0d"/>
      </linearGradient>
    </defs>
    <polygon points="224,31 660,31 660,96 282,96" fill="url(#footDark)"/>
    <polygon points="0,0 190,0 282,96 0,96" fill="url(#footRed)"/>
    <polygon points="190,0 196,0 288,96 282,96" fill="#fff"/>
  </svg>
  <div class="brand"><span class="mark"></span><span class="name">Brightfield Co</span></div>

  <div class="contact">
    <div class="phone">
      <span class="icon-ring"><svg width="9" height="9" viewBox="0 0 10 10"><path d="M2.2 1l1.6 1.9-.9 1.1q.8 1.7 2.6 2.6l1.1-.9L8.6 7.3 7.7 8.8Q4.5 9 1.8 5.5 0.6 3.4 1 2z" fill="#fff"/></svg></span>
      CALL US NOW: (866) 555-0172
    </div>
    <div class="lines">
      <span><span class="icon-ring"><svg width="9" height="9" viewBox="0 0 10 10"><circle cx="5" cy="5" r="4" fill="none" stroke="#fff"/><path d="M1 5h8M5 1q-2.5 4 0 8M5 1q2.5 4 0 8" fill="none" stroke="#fff" stroke-width=".8"/></svg></span>www.brightfieldvoices.example</span>
      <span><span class="icon-ring"><svg width="9" height="7" viewBox="0 0 10 8"><rect x=".5" y=".5" width="9" height="7" fill="none" stroke="#fff"/><path d="M.5 .5L5 4.5 9.5 .5" fill="none" stroke="#fff"/></svg></span>testimonials@brightfieldco.example</span>
    </div>
  </div>

</main>
</body>
</html>
```